Luxury Lifestyle Website - Blog and Product Showcasing

I am looking to create a simple, yet elegant website where I can post blog posts and feature products and brand partnerships for my company, Velmora Haus. I want a very elegant but not overly complex site. I like the look and feel of Corinne Ashdale's site - I don't need for it to be that robust or sophisticated, but that is the aesthetic I am going for. I would like to include my primary logo at the top of the main page, and also incorporate my alternative logos throughout the site in strategic places.

Target Market(s)

Luxury Brands; 20s-60s year olds; women; high-end fashion and tastes

Industry/Entity Type

Luxury Lifestyle - Blogging - Product Showcasing

Coding

Coded - Design and coding required

Number of Pages Required

4 page

Font styles to use
Sans Serif
Script
Other font styles liked:
• Pinyon

Colors
00AB8E
00BBA5
67D7C9
C6EFE9
E9F9F6
59FF00
82FF00
B8FF75
E3FFCB
F4FFEA

Requirements
Must have
• Creative use of my various logos. PASTEL GREENS or a DEEP DARK GREEN. Nothing bright, very soft and elegant.
Nice to have
• Elegant script that is easy to read.
Should not have
• Bright colors or overly modern look or feel.

```html
<!DOCTYPE html>
<html lang="en">
<head>
<meta charset="utf-8">
<title>Velmora Haus — Luxury Lifestyle</title>
<link href="https://fonts.googleapis.com/css2?family=Pinyon+Script&family=Tinos:wght@400;700&display=swap" rel="stylesheet">
<style>
:root{
  --paper:#f7f5f0;
  --white:#ffffff;
  --band:#ebe9e4;
  --ink:#2c2c2c;
  --muted:#555555;
  --rule:#d9d7d2;
  --teal:#00ab8e;
  --footer:#4a4a4a;
  --footer-text:#e8e8e8;
  --footer-muted:#c9c9c9;
  --product-bg:#f9f8f5;
}
*{box-sizing:border-box;margin:0;padding:0}
html,body{width:1200px;height:4854px;overflow:hidden}
body{background:var(--paper);font-family:"Tinos",serif;color:var(--ink);position:relative}
.script{font-family:"Pinyon Script",cursive;font-weight:400}
a{color:var(--teal);text-decoration:none;border-bottom:1px solid var(--teal);font-size:13px}

/* header */
.site-header{position:absolute;top:0;left:0;width:1200px;height:85px;background:var(--paper)}
.brand{position:absolute;left:88px;top:22px;display:flex;align-items:center;gap:14px}
.brand-mark{width:40px;height:40px;border:1px solid #6b6b6b}
.brand-name{font-size:23px;letter-spacing:1px;color:#4a4a4a}
.nav-icons{position:absolute;right:88px;top:28px;display:flex;align-items:center;gap:22px}
.shop-link{font-size:12px;color:#444;display:flex;align-items:center;gap:6px;position:relative}
.cart-badge{position:absolute;left:14px;top:-6px;width:12px;height:12px;border-radius:50%;background:var(--teal);color:#fff;font-size:8px;text-align:center;line-height:12px}

/* photo fills */
.photo{position:relative;overflow:hidden}

/* hero */
.hero{position:absolute;top:85px;left:0;width:1200px;height:631px;
  background:
    radial-gradient(ellipse 260px 340px at 640px 360px,rgba(196,128,82,.95),rgba(196,128,82,0) 70%),
    radial-gradient(ellipse 220px 260px at 170px 300px,rgba(92,104,70,.75),rgba(92,104,70,0) 70%),
    radial-gradient(ellipse 180px 160px at 1120px 470px,rgba(110,122,80,.55),rgba(110,122,80,0) 70%),
    linear-gradient(90deg,#c7a48c 0%,#d7c4b2 22%,#b98d6c 40%,#d8cbbd 62%,#eef0ee 72%,#e3e7e5 88%,#d7dcda 100%)}
.hero::after{content:"";position:absolute;left:0;right:0;bottom:0;height:150px;background:linear-gradient(180deg,rgba(240,236,230,0),rgba(226,218,208,.85))}
.hero-title{position:absolute;top:200px;width:1200px;text-align:center;color:#fff;font-size:88px;line-height:92px;z-index:1}

/* section header */
.section-head{position:absolute;left:88px;width:1024px;border-bottom:1px solid var(--rule);padding-bottom:10px;display:flex;justify-content:space-between;font-size:15px;letter-spacing:.5px}
.section-head a{font-size:12px}
.post-feature{position:absolute;left:0;width:1200px;text-align:center}
.post-feature h2{font-size:56px;line-height:66px;color:#333}
.post-feature p{font-size:13px;color:var(--muted);margin-top:24px}
.post-feature .more{display:inline-block;margin-top:44px}

/* categories */
.cat{position:absolute;top:1190px;width:321px}
.cat .photo{width:321px;height:385px}
.cat h3{font-weight:400;font-size:15px;margin-top:30px;letter-spacing:.4px}
.cat a{display:inline-block;margin-top:14px;font-size:12px}
.cat-lifestyle{background:
  radial-gradient(ellipse 90px 110px at 180px 200px,rgba(96,118,150,.55),rgba(96,118,150,0) 70%),
  radial-gradient(ellipse 130px 70px at 160px 360px,rgba(118,76,44,.9),rgba(118,76,44,0) 75%),
  linear-gradient(180deg,#a89884 0%,#c9bca8 38%,#b59d80 62%,#7e5a3c 100%)}
.cat-blogging{background:
  radial-gradient(ellipse 110px 120px at 150px 230px,rgba(250,250,248,.95),rgba(250,250,248,0) 75%),
  radial-gradient(ellipse 60px 70px at 200px 200px,rgba(90,110,80,.55),rgba(90,110,80,0) 70%),
  linear-gradient(180deg,#cdbfae 0%,#e2d8cc 45%,#a5876a 80%,#7b5e44 100%)}
.cat-product{background:
  radial-gradient(ellipse 200px 60px at 160px 300px,rgba(118,72,40,.95),rgba(118,72,40,0) 80%),
  linear-gradient(115deg,#f0ede8 0%,#e4ded5 45%,#cfc5b7 60%,#e8e3dc 75%,#b6a690 100%)}

/* chapter */
.chapter{position:absolute;top:1745px;left:0;width:1200px;height:546px;background:var(--white)}
.chapter .photo{position:absolute;left:0;top:0;width:667px;height:546px;background:
  radial-gradient(ellipse 150px 210px at 320px 380px,rgba(140,124,104,.9),rgba(140,124,104,0) 72%),
  radial-gradient(ellipse 70px 70px at 320px 150px,rgba(74,58,48,.85),rgba(74,58,48,0) 75%),
  radial-gradient(ellipse 90px 200px at 500px 220px,rgba(176,140,96,.75),rgba(176,140,96,0) 75%),
  linear-gradient(180deg,#ebe8e3 0%,#e3dfd8 70%,#c9b79c 88%,#a88c6c 100%)}
.chapter-text{position:absolute;left:750px;width:360px;top:88px;text-align:center}
.chapter-text .kicker{font-size:15px;letter-spacing:.5px}
.chapter-text h2{font-size:52px;margin-top:8px;color:#333}
.chapter-text p{font-size:13px;line-height:24px;color:var(--muted);margin-top:20px}
.chapter-text a{display:inline-block;margin-top:44px}

/* shop */
.shop{position:absolute;top:2766px;left:0;width:1200px;height:618px;background:var(--band);text-align:center}
.shop h2{font-size:58px;position:absolute;top:66px;width:100%;color:#333}
.shop .sub{position:absolute;top:148px;width:100%;font-size:14px;letter-spacing:.4px}
.product{position:absolute;top:188px;width:285px;height:332px;background:var(--product-bg)}
.product .photo{position:absolute;left:38px;top:24px;width:209px;height:200px;border-radius:4px}
.product-perfume{background:linear-gradient(180deg,#f9f8f5 0%,#f6e4ee 30%,#ee9fcb 62%,#f3c9df 82%,#f9f8f5 100%)}
.product-powder{background:linear-gradient(180deg,#f9f8f5 0%,#e6dfe4 28%,#5a4a46 55%,#2a2220 75%,#f9f8f5 100%)}
.product-bowl{background:linear-gradient(180deg,#f9f8f5 0%,#f2e6cc 32%,#e4b66e 56%,#c9633c 74%,#f9f8f5 100%)}
.product .btn{position:absolute;left:68px;top:262px;width:140px;height:36px;border:1px solid #333;font-size:13px;line-height:34px;color:#333}
.shop .visit{position:absolute;top:556px;left:557px}

/* videos */
.videos h2{position:absolute;top:3440px;width:1200px;text-align:center;font-size:56px;color:#333}
.video{position:absolute;top:3527px;height:307px}
.video-cosy{background:
  radial-gradient(ellipse 50px 45px at 75px 250px,rgba(212,108,56,.95),rgba(212,108,56,0) 75%),
  radial-gradient(ellipse 80px 140px at 240px 130px,rgba(236,226,212,.95),rgba(236,226,212,0) 75%),
  linear-gradient(135deg,#3e332c 0%,#5a4a3e 30%,#c8b39c 55%,#e6dccf 100%)}
.video-studio{background:
  radial-gradient(ellipse 60px 70px at 220px 200px,rgba(230,150,170,.8),rgba(230,150,170,0) 75%),
  radial-gradient(ellipse 60px 110px at 80px 150px,rgba(246,244,240,1),rgba(246,244,240,0) 75%),
  linear-gradient(180deg,#ecebe7 0%,#e2ddd5 60%,#a67b5a 85%,#8a6246 100%)}
.video-sofa{background:
  radial-gradient(ellipse 170px 70px at 200px 250px,rgba(54,36,30,.95),rgba(54,36,30,0) 80%),
  radial-gradient(ellipse 110px 45px at 160px 60px,rgba(180,136,96,.9),rgba(180,136,96,0) 80%),
  linear-gradient(180deg,#ddd4c8 0%,#e4ddd3 45%,#6a4c40 80%,#3c2a24 100%)}
.play{position:absolute;left:50%;top:50%;width:64px;height:64px;margin:-32px 0 0 -32px;border-radius:50%;background:rgba(60,60,60,.55)}
.play::after{content:"";position:absolute;left:27px;top:24px;border-left:12px solid #fff;border-top:8px solid transparent;border-bottom:8px solid transparent}

.article{position:absolute;top:3955px;width:1200px;text-align:center}
.article h3{font-weight:400;font-size:16px;letter-spacing:.5px}
.article p{font-size:13px;color:var(--muted);margin-top:14px}
.article a{display:inline-block;margin-top:38px}

.gallery{position:absolute;top:4120px;left:88px;display:flex;gap:8px}
.gallery div{width:139px;height:176px}

/* footer */
.site-footer{position:absolute;top:4437px;left:0;width:1200px;height:417px;background:var(--footer);color:var(--footer-text)}
.footer-brand{position:absolute;left:110px;top:116px;width:300px;text-align:center}
.footer-brand .brand-mark{width:90px;height:90px;border:1px solid #bdbdbd;margin:0 auto 14px}
.footer-brand .name{font-size:30px;letter-spacing:1.5px}
.socials{display:flex;justify-content:center;gap:10px;margin-top:22px}
.socials span{width:32px;height:32px;border-radius:50%;background:#5e5e5e;display:block}
.footer-col{position:absolute;top:86px}
.footer-col h4{font-weight:700;font-size:17px;letter-spacing:.5px;margin-bottom:16px}
.footer-col li{list-style:none;font-size:12px;line-height:26px;color:var(--footer-muted)}
.field{width:228px;border-bottom:1px solid #8a8a8a;font-size:11px;color:var(--footer-muted);padding:12px 0 4px}
.footer-col .subscribe{display:inline-block;margin-top:14px;font-size:12px}
.footer-rule{position:absolute;left:88px;top:358px;width:1024px;border-top:1px solid #5f5f5f}
.copyright{position:absolute;top:382px;width:100%;text-align:center;font-size:12px}
.to-top{position:absolute;left:1132px;top:340px;width:40px;height:40px;border-radius:50%;background:var(--teal)}
.to-top::after{content:"";position:absolute;left:15px;top:17px;border-bottom:6px solid #fff;border-left:5px solid transparent;border-right:5px solid transparent}
</style>
</head>
<body>

<header class="site-header">
  <div class="brand"><span class="brand-mark"></span><span class="brand-name">VELMORA HAUS</span></div>
  <nav class="nav-icons">
    <svg width="24" height="20" viewBox="0 0 24 20"><path d="M2 3h20M8 10h14M2 17h20" stroke="#333" stroke-width="2"/></svg>
    <svg width="20" height="20" viewBox="0 0 20 20"><circle cx="8" cy="8" r="6" fill="none" stroke="#333" stroke-width="2"/><path d="M13 13l5 5" stroke="#333" stroke-width="2"/></svg>
    <span class="shop-link">
      <svg width="22" height="20" viewBox="0 0 22 20"><path d="M1 2h4l3 11h11l2-8H7" fill="none" stroke="#333" stroke-width="1.6"/><circle cx="9" cy="17" r="1.6" fill="#333"/><circle cx="17" cy="17" r="1.6" fill="#333"/></svg>
      <span class="cart-badge">0</span>SHOP
    </span>
  </nav>
</header>

<section class="hero" role="img" aria-label="Woman in a hat sitting on a window ledge beside potted plants">
  <h1 class="hero-title script">Velmora Haus<br>Luxury lifestyle</h1>
</section>

<div class="section-head" style="top:783px"><span>FEATURED POST</span><a href="#">Read All Posts</a></div>
<article class="post-feature" style="top:870px">
  <h2 class="script">Some Velmora Haus<br>Luxury lifestyle</h2>
  <p>Aenean sollicitudin lorem quis bibendum auctor nisi elit consequat ipsum nec sagittis...</p>
  <a class="more" href="#">Read On</a>
</article>

<div class="cat" style="left:88px"><div class="photo cat-lifestyle" role="img" aria-label="Woman relaxing in an armchair in a sunlit room"></div><h3>LUXURY LIFESTYLE</h3><a href="#">Read All</a></div>
<div class="cat" style="left:439px"><div class="photo cat-blogging" role="img" aria-label="Woman working on a laptop on a white sofa"></div><h3>BLOGGING</h3><a href="#">Read All</a></div>
<div class="cat" style="left:791px"><div class="photo cat-product" role="img" aria-label="Candle holder and cup on a wooden table"></div><h3>PRODUCT SHOWCASING</h3><a href="#">Read All</a></div>

<section class="chapter">
  <div class="photo" role="img" aria-label="Woman seen from behind at a desk beside dried pampas grass"></div>
  <div class="chapter-text">
    <div class="kicker">CHAPTER 1</div>
    <h2 class="script">September</h2>
    <p>Aenean sollicitudin, lorem quis bibendum auctor, nisi elit consequat ipsum nec sagittis sem nibh id elit. Duis sed odio sit amet nibh vulputate cursus a sit amet mauris. Morbi accumsan ipsum velit. Nam nec tellus a odio tincidunt auctor a ornare odio. Sed non mauris vitae erat consequat auctor eu in elit. Class aptent taciti sociosqu ad litora torquent per conubia nostra, per inceptos himenaeos mauris in erat justo...</p>
    <a href="#">All Chapter</a>
  </div>
</section>

<div class="section-head" style="top:2358px"><span>RECENT POST</span><a href="#">Read All Posts</a></div>
<article class="post-feature" style="top:2445px">
  <h2 class="script">Some Velmora Haus<br>Luxury lifestyle</h2>
  <p>Aenean sollicitudin lorem quis bibendum auctor nisi elit consequat ipsum nec sagittis...</p>
  <a class="more" href="#">Read On</a>
</article>

<section class="shop">
  <h2 class="script">My Shop</h2>
  <div class="sub">THINGS THAT HAVE CAUGHT MY EYE RECENTLY...</div>
  <div class="product" style="left:154px"><div class="photo product-perfume" role="img" aria-label="Pink perfume bottle"></div><span class="btn">Shop Now</span></div>
  <div class="product" style="left:458px"><div class="photo product-powder" role="img" aria-label="Dark cosmetic jar with powder"></div><span class="btn">Shop Now</span></div>
  <div class="product" style="left:761px"><div class="photo product-bowl" role="img" aria-label="Porcelain bowl of noodles with chopsticks"></div><span class="btn">Shop Now</span></div>
  <a class="visit" href="#">Visit My Shop</a>
</section>

<section class="videos">
  <h2 class="script">Recent Videos</h2>
  <div class="video video-cosy" style="left:88px;width:336px" role="img" aria-label="Cosy scene with coffee, knit socks and a pumpkin"><span class="play"></span></div>
  <div class="video video-studio" style="left:431px;width:338px" role="img" aria-label="Man sitting on the floor with a cat beside a large vase"><span class="play"></span></div>
  <div class="video video-sofa" style="left:776px;width:336px" role="img" aria-label="Woman using a laptop on a leather sofa"><span class="play"></span></div>
</section>

<article class="article">
  <h3>MY NOT SO SUNNY SUMMER WARDROBE STAPLES...</h3>
  <p>For the rainy days when 'summer in Britain' lives up to its not-so-sunny reputation...</p>
  <a href="#">Read On</a>
</article>

<div class="gallery">
  <div role="img" aria-label="Woman at a table" style="background:linear-gradient(180deg,#e6ddd2 0%,#c79a7c 45%,#7e8a6c 75%,#b6a48e 100%)"></div>
  <div role="img" aria-label="Book and coffee on a pink quilt" style="background:linear-gradient(180deg,#eee8e1 0%,#f6f3ef 35%,#dcbab0 65%,#c99d94 100%)"></div>
  <div role="img" aria-label="Woman arranging flowers" style="background:linear-gradient(180deg,#eae6df 0%,#d4cbbf 35%,#3d3f4a 65%,#b9453e 100%)"></div>
  <div role="img" aria-label="Vase with dried branches on a sideboard" style="background:linear-gradient(180deg,#f1efeb 0%,#e6e2dc 45%,#a9805c 70%,#7d5a3e 100%)"></div>
  <div role="img" aria-label="Woman reading in an armchair" style="background:linear-gradient(180deg,#8b9478 0%,#cfccc2 40%,#e9e4dc 70%,#b9aa98 100%)"></div>
  <div role="img" aria-label="White side table with plant" style="background:linear-gradient(180deg,#e9e7e2 0%,#7f9168 35%,#f4f3f0 65%,#d8d4cc 100%)"></div>
  <div role="img" aria-label="Woman in a rust sweater" style="background:linear-gradient(180deg,#efe9e1 0%,#e2d2c2 35%,#c4693a 65%,#a9542e 100%)"></div>
</div>

<footer class="site-footer">
  <div class="footer-brand">
    <div class="brand-mark"></div>
    <div class="name">VELMORA HAUS</div>
    <div class="socials"><span aria-label="Social link"></span><span aria-label="Social link"></span><span aria-label="Social link"></span><span aria-label="Social link"></span><span aria-label="Social link"></span></div>
  </div>
  <div class="footer-col" style="left:477px"><h4>ABOUT</h4><ul><li>Velmora Haus</li><li>FAQ</li><li>Contact</li><li>Shop</li><li>Privacy Policy</li></ul></div>
  <div class="footer-col" style="left:635px"><h4>TOPICS</h4><ul><li>Luxury Lifestyle</li><li>Blogging</li><li>Product Showcasing</li></ul></div>
  <div class="footer-col" style="left:840px"><h4>NEWSLETTER</h4><ul><li>Get Updates &amp; Exclusive News</li></ul>
    <div class="field">First name</div><div class="field">Email address</div><a class="subscribe" href="#">Subscribe</a></div>
  <div class="footer-rule"></div>
  <span class="to-top"></span>
  <div class="copyright">© Copyright 2023 Velmora Haus All Rights Reserved</div>
</footer>

</body>
</html>
```